HOT TUB - SPAS service needs an business card

I need an business for my company who his specialise in a maintenance,water treatment and cleaning of Hot Tub - Spas for commercial and residential customers. The company operate mainly in the ski resort of Chamonix, Megève and St Gervais. The final product should communicate pure water, cleanest and professional for luxury property's.
I have upload a logo but any improvement on it is welcome.(color,size, details etc..) or any other idea. Thank you
Company Name: 58 BAINS
My name: Laurent Mazeyrac
Email: lmazey@courrielo.fr
Tel: +33 (0)6 81 52 29 07
Description to be on the card in french(first langage) and in English:
- Spas service
- Entretien, traitement eau, nettoyage.
- Maintenance, water treatment, cleaning.

```html
<!DOCTYPE html>
<html lang="fr">
<head>
<meta charset="utf-8">
<title>58 BAINS – Cartes de visite</title>
<link href="https://fonts.googleapis.com/css2?family=Titan+One&family=Didact+Gothic&family=Source+Sans+3:wght@400&display=swap" rel="stylesheet">
<style>
  :root {
    --bg: #e9e7e4;
    --card: #ffffff;
    --navy: #3f4ea0;
    --sky: #72b4e2;
    --ice: #d4e8f6;
    --steam: #c9cacc;
    --white: #ffffff;
  }
  * { margin: 0; padding: 0; box-sizing: border-box; }
  html, body {
    width: 1200px; height: 1000px; overflow: hidden;
    background: var(--bg);
  }
  .stage { position: relative; width: 1200px; height: 1000px; }
  .card {
    position: absolute; left: 220px;
    width: 760px; height: 440px;
    background: var(--card);
    border-radius: 34px;
    overflow: hidden;
    box-shadow: 0 6px 18px rgba(0,0,0,.18);
  }
  .card--front { top: 45px; }
  .card--back { top: 515px; }

  /* front */
  .front__art {
    position: absolute; left: 210px; top: 40px;
    width: 340px; height: 160px;
    border-radius: 10px;
    background: linear-gradient(135deg, var(--navy) 0%, var(--sky) 55%, var(--ice) 100%);
  }
  .brand {
    font-family: "Titan One", serif;
    font-weight: 400;
    color: var(--navy);
    letter-spacing: 1px;
  }
  .front__brand {
    position: absolute; left: 0; right: 0; top: 205px;
    text-align: center; font-size: 74px; line-height: 1;
  }
  .front__band {
    position: absolute; left: 0; right: 0; bottom: 0; height: 100px;
    background: var(--navy);
    border-top: 12px solid var(--sky);
  }
  .services {
    display: flex; justify-content: space-between;
    padding: 14px 70px 0 110px;
    font-family: "Didact Gothic", sans-serif;
    color: var(--white); font-size: 24px; line-height: 1.15;
  }

  /* back */
  .back__brand {
    position: absolute; left: 90px; top: 40px;
    font-size: 58px; line-height: 1;
  }
  .back__name {
    position: absolute; left: 90px; top: 118px;
    font-family: "Source Sans 3", sans-serif;
    font-size: 33px; color: var(--navy);
  }
  .back__wave { position: absolute; left: 0; top: 0; width: 760px; height: 440px; }
  .back__art {
    position: absolute; left: 470px; top: 40px;
    width: 250px; height: 310px;
    border-radius: 14px;
    background: linear-gradient(180deg, rgba(201,202,204,.55) 0%, var(--ice) 65%, var(--sky) 100%);
  }
  .contact {
    position: absolute; left: 60px; top: 290px;
    list-style: none;
    font-family: "Source Sans 3", sans-serif;
    font-size: 29px; color: var(--white); line-height: 1.5;
  }
  .contact__item { display: flex; align-items: center; gap: 12px; }
  .contact__icon { width: 22px; height: 26px; flex: none; }
</style>
</head>
<body>
<main class="stage">

  <section class="card card--front">
    <div class="front__art" role="img" aria-label="Illustration de montagnes enneigées, d'un chalet et d'un spa fumant"></div>
    <div class="brand front__brand">58 BAINS</div>
    <div class="front__band">
      <div class="services">
        <span>Entretien,<br>Maintenance,</span>
        <span>traitement eau,<br>water treatment,</span>
        <span>nettoyage.<br>cleaning.</span>
      </div>
    </div>
  </section>

  <section class="card card--back">
    <svg class="back__wave" viewBox="0 0 760 440" aria-hidden="true">
      <path d="M0 250 C120 190 260 200 380 280 C470 340 600 330 760 300 L760 440 L0 440 Z" fill="var(--navy)"/>
    </svg>
    <div class="back__art" role="img" aria-label="Illustration d'un spa vu de dessus avec de la vapeur"></div>
    <div class="brand back__brand">58 BAINS</div>
    <div class="back__name">Laurent Mazeyrac</div>
    <ul class="contact">
      <li class="contact__item">
        <svg class="contact__icon" viewBox="0 0 22 26" aria-hidden="true">
          <rect x="5" y="1" width="12" height="24" rx="2" fill="none" stroke="#fff" stroke-width="2"/>
          <line x1="9" y1="21" x2="13" y2="21" stroke="#fff" stroke-width="2"/>
        </svg>
        +33 (0)6 81 52 29 07
      </li>
      <li class="contact__item">
        <svg class="contact__icon" viewBox="0 0 22 26" aria-hidden="true">
          <rect x="1" y="6" width="20" height="14" fill="none" stroke="#fff" stroke-width="2"/>
          <path d="M1 6 L11 14 L21 6" fill="none" stroke="#fff" stroke-width="2"/>
        </svg>
        lmazey@courrielo.fr
      </li>
    </ul>
  </section>

</main>
</body>
</html>
```